Business Card for Yachting Management Company

Need a business card design for a new yachting project management company. Attached is the logo for the company.
Our clients are large yacht owners and captains.
Design must be in the style of the logo. Modern, elegant.

Example of data to show:
Peter Hollis
Project Manager
(+34) 612 738 104
peter@quorvane.net
Quorvane Management - Meridel Tower, Office 22 - KRB - Palma de Mallorca

The data above will have to be changed (by me) for the different people in the company over the next years.

Will be printed using PrintNova (Lustre Card Series). They provide these guidelines for the size:
"the actual size of the card is 1050 x 600 pixels. However, the full bleed size is 1083 x 633 pixels, and the safe printing area is 1008 x 558 pixels."

```html
<!DOCTYPE html>
<html lang="en">
<head>
<meta charset="utf-8">
<title>Quorvane Management – Business Card</title>
<link rel="stylesheet" href="https://fonts.googleapis.com/css2?family=Roboto:wght@400;700&display=swap">
<style>
  :root {
    --page-bg: #ababab;
    --card-bg: #242424;
    --accent-shape: #484848;
    --brand-blue: #0a6fc2;
    --text-white: #ffffff;
    --text-muted: #8c8c8c;
  }
  html, body {
    margin: 0;
    padding: 0;
    width: 1200px;
    height: 1000px;
    overflow: hidden;
    background: var(--page-bg);
    font-family: "Roboto", Arial, sans-serif;
  }
  .canvas {
    position: relative;
    width: 1200px;
    height: 1000px;
  }
  .card {
    position: absolute;
    left: 343px;
    width: 514px;
    height: 296px;
    background: var(--card-bg);
    overflow: hidden;
  }
  .card--front { top: 152px; }
  .card--back  { top: 504px; }
  .card-shape {
    position: absolute;
    inset: 0;
    width: 514px;
    height: 296px;
  }
  .card-shape polygon { fill: var(--accent-shape); }
  .brand-name {
    position: absolute;
    color: var(--brand-blue);
    font-weight: 700;
    line-height: 1;
    letter-spacing: 0.02em;
  }
  .brand-name .brand-main {
    display: block;
    font-size: 21px;
  }
  .brand-name .brand-sub {
    display: block;
    font-size: 9px;
    letter-spacing: 0.28em;
    margin-top: 5px;
  }
  .card--front .brand-name { left: 27px; top: 36px; }
  .card--back .brand-name { right: 22px; bottom: 24px; text-align: right; }
  .contact {
    position: absolute;
    left: 28px;
    top: 111px;
    font-size: 16px;
    line-height: 19px;
    color: var(--text-muted);
  }
  .contact p { margin: 0; }
  .contact .person-name { color: var(--brand-blue); font-weight: 700; }
  .contact .person-role { color: var(--text-white); }
  .contact .address { margin-top: 19px; }
</style>
</head>
<body>
<main class="canvas">
  <section class="card card--front" aria-label="Business card front">
    <svg class="card-shape" viewBox="0 0 514 296" aria-hidden="true">
      <polygon points="496,19 496,278 305,278"/>
    </svg>
    <div class="brand-name">
      <span class="brand-main">Quorvane</span>
      <span class="brand-sub">MANAGEMENT</span>
    </div>
    <div class="contact">
      <p class="person-name">Peter Hollis</p>
      <p class="person-role">Project Manager</p>
      <p>(+34) 612 738 104</p>
      <p>peter@quorvane.net</p>
      <div class="address">
        <p>Meridel Tower,</p>
        <p>Office 22 - KRB</p>
        <p>Palma de Mallorca</p>
      </div>
    </div>
  </section>

  <section class="card card--back" aria-label="Business card back">
    <svg class="card-shape" viewBox="0 0 514 296" aria-hidden="true">
      <polygon points="18,18 209,18 18,278"/>
    </svg>
    <div class="brand-name">
      <span class="brand-main">Quorvane</span>
      <span class="brand-sub">MANAGEMENT</span>
    </div>
  </section>
</main>
</body>
</html>
```